Flyers needed for new business Tidebloom

We have a colour and business & loyalty card currently on file, we would Ike similar colours and styles, flyers I think we make 3 folding,

Target Market(s)

We specialise in Magnesium float, infared saunas and hyperbaric oxygen chamber, all this is targeted for clients trying to manage chronic pain, weigh loss and detoxification

Industry/Entity Type

Health And Wellness

Font styles to use
Sans Serif
Decorative

Colors
33a6d7
85cae6
ffffff
9d9d9d

Requirements
Must have
• Business name an logo on front, middle I think we outline facilities and business outline, we are here to help our clients become their best selves through using our facilities we can assist them in the own journeys to becoming better able to manage chronic pain, weight loss that seems impossible to lose and provide the best meditative float experience they ever experienced
Nice to have
• Some photos of magnesium float tank, infrared sauna & oxygen chamber

```html
<!DOCTYPE html>
<html lang="en">
<head>
<meta charset="utf-8">
<title>Tidebloom Tri-fold Brochure</title>
<link href="https://fonts.googleapis.com/css2?family=Bebas+Neue&family=Mulish:wght@400;600;700&display=swap" rel="stylesheet">
<style>
:root{
  --blue:#33a6d7;
  --blue-deep:#1f8fc4;
  --blue-soft:#85cae6;
  --white:#ffffff;
  --grey:#9d9d9d;
  --ink:#2e2e2e;
  --stage:#f2f2f2;
}
*{margin:0;padding:0;box-sizing:border-box}
html,body{width:1200px;height:1000px;overflow:hidden}
body{background:linear-gradient(#ffffff,var(--stage));font-family:"Mulish",sans-serif;position:relative}
.spread{position:absolute;left:278px;width:685px;height:484px;display:flex;box-shadow:0 2px 6px rgba(0,0,0,.25)}
.spread--outside{top:8px}
.spread--inside{top:504px}
.panel{position:relative;width:228.33px;height:100%;overflow:hidden}
.panel--blue{background:linear-gradient(90deg,var(--blue) 70%,var(--blue-deep));color:var(--white)}
.panel--paper{background:linear-gradient(90deg,#ffffff 35%,#e4e4e4 80%,#bdbdbd);color:var(--ink)}
.panel--paper-light{background:linear-gradient(90deg,#cfcfcf,#f7f7f7 12%,#ffffff);color:var(--ink)}
.abs{position:absolute}
.bar{position:absolute;height:4px;background:var(--white)}
.bar--dark{background:var(--ink)}
.heading{font-family:"Bebas Neue",sans-serif;font-weight:400;line-height:1;letter-spacing:.2px}
.body-copy{font-size:8.6px;line-height:11.4px;text-align:justify}
.subtitle{font-size:11.5px;font-weight:400}
/* about */
.about-title{left:22px;top:37px;font-size:24px}
.about-text{left:22px;top:72px;width:187px}
.about-rule{left:22px;top:268px;width:187px;height:1px;background:var(--white);position:absolute}
.about-sub{left:22px;top:281px}
.about-text2{left:22px;top:304px;width:187px}
/* contact */
.contact{text-align:center;left:0;width:228px}
.contact-title{top:84px;font-size:23px;color:var(--ink)}
.contact-intro{top:112px;font-size:8.6px;line-height:11.4px;padding:0 30px}
.contact-rule{left:24px;top:159px;width:181px;height:1px;background:#555;position:absolute}
.contact-item{position:absolute;left:0;width:228px;text-align:center;font-size:11px;color:var(--ink)}
.contact-item svg{display:block;margin:0 auto 4px}
.contact-tab{left:27px;top:459px;width:176px;height:25px;background:var(--blue)}
/* cover */
.cover-photo{inset:0;background:radial-gradient(ellipse at 70% 25%,#5cbde6,var(--blue) 45%,#1c86bd);position:absolute}
.brand{left:17px;top:25px;font-size:19px;font-weight:700;line-height:19px;color:var(--white);letter-spacing:.5px}
.cover-bar{right:20px;top:276px;width:62px}
.cover-headline{right:20px;top:290px;text-align:right;font-size:40px;line-height:49px;color:var(--white)}
.cover-sub{right:20px;top:430px;text-align:right;font-size:12px;line-height:15px;color:var(--white)}
/* why float */
.why-photo{left:0;top:0;width:228px;height:159px;background:radial-gradient(circle at 45% 45%,#d8d8d8,#8d8d8d 75%);position:absolute}
.why-title{left:22px;top:187px;font-size:23px}
.why-list{left:22px;top:222px;width:187px}
.why-list h3{font-size:11.5px;font-weight:400;margin-bottom:5px}
.why-list p{margin-bottom:12px}
/* how */
.how-bar{left:21px;top:26px;width:57px}
.how-title{left:21px;top:36px;font-size:23px}
.how-text{left:21px;top:69px;width:192px}
.step{position:absolute;left:18px;display:flex;align-items:center;gap:9px}
.step h3{font-size:11px;font-weight:400;margin-bottom:3px}
.step p{font-size:8.6px}
/* facilities */
.fac-bar{left:14px;top:26px;width:57px}
.fac-title{left:14px;top:36px;font-size:23px}
.fac-photo{position:absolute;left:17px;width:185px;height:85px}
.fac-label{position:absolute;left:17px;font-size:8.8px;letter-spacing:.3px}
.fac-rule{left:15px;top:425px;width:188px;height:1px;background:#555;position:absolute}
.fac-text{left:15px;top:430px;width:188px}
</style>
</head>
<body>

<section class="spread spread--outside">
  <article class="panel panel--blue">
    <div class="bar" style="left:22px;top:27px;width:57px"></div>
    <h2 class="heading abs about-title">About Us</h2>
    <p class="body-copy abs about-text">Lorem ipsum dolor sit amet, consectetur adip. Quisque non fringilla sapien, et viverra nulla. Nam sollicitudin arcu non aliquet porta. Sus pendisse a mauris risus. Donec sed ipsum est. Mauris risus neque, mattis eu tempor in, ul trices id nisl. Lorem ipsum dolor sit amet, con sectetur adipiscing elit. Ut pulvinar libero at lo bortis ornare. Fusce quis orci ac massa tempor tristique sed vitae magna. Curabitur ut urna. Nullam pharetra vestibulum mauris, a tempor dolor molestie sit amet. Curabitur vehicula el ementum ex, ut posuere ex commodo et.<br><br>Quisque vitae facilisis urna, vitae dapibus tortor. Nulla eu elit ex. Pellentesque eu semper nulla.</p>
    <div class="about-rule"></div>
    <h3 class="subtitle abs about-sub">Your Title Here</h3>
    <p class="body-copy abs about-text2">Integer sit amet interdum ligula. Aenean com modo nunc non tempor tempor. Curabitur id tempus nibh. Phasellus non est massa. Pellen tesque ut bibendum mauris, scelerisque max imus quam. Aliquam orci arcu, pharetra vel purus a, maximus molestie libero.<br><br>Nam lacinia ligula molestie, blandit dui ac, bibendum eros. Sed maximus ullamcorper lorem, vitae interdum mi dignissim eget. Sed congue felis in iaculis vehicula. Vivamus vulp tate ligula vel tellus vehicula, vel venenatis nisi suscipit.</p>
  </article>

  <article class="panel panel--paper">
    <svg class="abs" style="left:92px;top:28px" width="46" height="44" viewBox="0 0 46 44" fill="none" stroke="var(--blue)" stroke-width="3">
      <path d="M6 4h20a4 4 0 0 1 4 4v10a4 4 0 0 1-4 4H14l-7 6v-6H6a4 4 0 0 1-4-4V8a4 4 0 0 1 4-4z"/>
      <path d="M20 18h18a4 4 0 0 1 4 4v10a4 4 0 0 1-4 4h-1v6l-7-6H20a4 4 0 0 1-4-4V22" fill="var(--white)"/>
      <circle cx="23" cy="27" r="1" fill="var(--blue)"/><circle cx="29" cy="27" r="1" fill="var(--blue)"/><circle cx="35" cy="27" r="1" fill="var(--blue)"/>
    </svg>
    <h2 class="heading abs contact contact-title">Get In Touch</h2>
    <p class="abs contact contact-intro">Please feel free to call or email us. We'd love to hear your thoughts and answer any questions you may have!</p>
    <div class="contact-rule"></div>
    <div class="contact-item" style="top:178px">
      <svg width="20" height="20" viewBox="0 0 20 20" fill="none" stroke="var(--ink)" stroke-width="1.4"><circle cx="10" cy="10" r="9"/><path d="M7 5.5l1.5 2.5-1 1.2c.6 1.3 1.5 2.2 2.8 2.8l1.2-1 2.5 1.5-.8 1.6c-3.5-.2-6.6-3.3-6.8-6.8z" fill="var(--ink)"/></svg>
      (123) 456 7890
    </div>
    <div class="contact-item" style="top:227px">
      <svg width="20" height="20" viewBox="0 0 20 20" fill="none" stroke="var(--ink)" stroke-width="1.4"><circle cx="10" cy="10" r="9"/><rect x="5" y="6.5" width="10" height="7"/><path d="M5 6.5l5 4 5-4"/></svg>
      hello@tidebloom.com
    </div>
    <div class="contact-item" style="top:278px">
      <svg width="20" height="20" viewBox="0 0 20 20" fill="none" stroke="var(--ink)" stroke-width="1.3"><circle cx="10" cy="10" r="8"/><ellipse cx="10" cy="10" rx="3.5" ry="8"/><path d="M2 10h16M3.5 6h13M3.5 14h13"/></svg>
      www.tidebloom.com
    </div>
    <div class="contact-item" style="top:328px">
      <svg width="20" height="20" viewBox="0 0 20 20" fill="none" stroke="var(--ink)" stroke-width="1.4"><circle cx="10" cy="10" r="9"/></svg>
      tidebloom
    </div>
    <div class="contact-item" style="top:379px">
      <svg width="20" height="20" viewBox="0 0 20 20" fill="none" stroke="var(--ink)" stroke-width="1.4"><circle cx="10" cy="10" r="9"/></svg>
      social/tidebloom
    </div>
    <div class="abs contact-tab"></div>
  </article>

  <article class="panel">
    <div class="cover-photo" role="img" aria-label="Photo of a woman floating relaxed on her back in bright blue water"></div>
    <p class="abs brand">TIDEBLOOM</p>
    <div class="bar cover-bar"></div>
    <h1 class="heading abs cover-headline">Your Next<br>Level Of<br>Relaxation.</h1>
    <p class="abs cover-sub">Reset your mind and body<br>with Magnesium float pool.</p>
  </article>
</section>

<section class="spread spread--inside">
  <article class="panel panel--blue">
    <div class="why-photo" role="img" aria-label="Black and white aerial photo of a woman floating in a pool"></div>
    <div class="bar" style="left:22px;top:174px;width:57px"></div>
    <h2 class="heading abs why-title">Why Float?</h2>
    <div class="abs why-list body-copy">
      <h3>Chronic Pain Management</h3>
      <p>Integer sit amet interdum ligula. Aenean com modo nunc non tempor tempor. Curabitur id tempus nibh.</p>
      <h3>Helps Lose Weight</h3>
      <p>Nam lacinia ligula molestie, blandit dui ac, bibendum eros. Sed maximus ullamcorper lorem, vitae.</p>
      <h3>Reduces Stress</h3>
      <p>Pellentesque vel massa in dui convallis aliquet. Etiam nibh ligula, tincidunt sit amet ligula vitae, faucibus feugiat nunc.</p>
      <h3>Improves Sleep</h3>
      <p>Ulla condimentum massa sit amet quam fringil la vehicula. Sed auctor, turpis porta faucibus pharetra, dui arcu ornare ulma.</p>
    </div>
  </article>

  <article class="panel panel--paper">
    <div class="bar bar--dark how-bar"></div>
    <h2 class="heading abs how-title">How It Works</h2>
    <p class="body-copy abs how-text">Maecenas egestas nunc nisi, ut ultricies elit he ndrerit non. Pellentesque vel lorem eget tellus tristique scelerisque vel eget ligula. Donec ac pellentesque mi. Nam ullamcorper tellus.</p>

    <div class="step" style="top:128px">
      <svg width="40" height="48" viewBox="0 0 40 48" fill="none" stroke="var(--blue)" stroke-width="1.8"><path d="M20 2v6M8 24a12 12 0 0 1 24 0z"/><path d="M6 24h28"/><path d="M12 30v5M17 30v8M23 30v8M28 30v5M20 40v6M14 40v3M26 40v3"/></svg>
      <div><h3>Your Title Here</h3><p>Phasellus non est massa.</p></div>
    </div>
    <div class="step" style="top:196px">
      <svg width="40" height="46" viewBox="0 0 40 46" fill="none" stroke="var(--blue)" stroke-width="1.8"><path d="M20 8a11 11 0 0 0-6 20v6h12v-6a11 11 0 0 0-6-20z"/><path d="M15 38h10M16 42h8M20 1v3M6 8l2 2M34 8l-2 2M2 20h3M35 20h3"/></svg>
      <div><h3>Your Title Here</h3><p>Sed congue felis in iaculis vehicula.</p></div>
    </div>
    <div class="step" style="top:266px">
      <svg width="44" height="40" viewBox="0 0 44 40" fill="none" stroke="var(--blue)" stroke-width="1.8"><ellipse cx="18" cy="20" rx="16" ry="16"/><path d="M4 14c8 5 20 5 28 0M4 26c8-5 20-5 28 0"/><circle cx="38" cy="10" r="3" fill="var(--blue)"/><path d="M38 14v12M34 18h8" /></svg>
      <div><h3>Your Title Here</h3><p>Curabitur tinci dunt, urna ac lobo.</p></div>
    </div>
    <div class="step" style="top:336px">
      <svg width="44" height="40" viewBox="0 0 44 40" fill="none" stroke="var(--blue)" stroke-width="1.8"><path d="M4 6l4-3 4 3 4-3 4 3 4-3 4 3 4-3 4 3 4-3M4 36l4-3 4 3 4-3 4 3 4-3 4 3 4-3 4 3 4-3"/><rect x="4" y="16" width="30" height="7" fill="var(--blue)" stroke="none"/><circle cx="38" cy="19.5" r="4" fill="var(--blue)" stroke="none"/></svg>
      <div><h3>Your Title Here</h3><p>Morbi tristique id massa id.</p></div>
    </div>
    <div class="step" style="top:408px">
      <svg width="44" height="42" viewBox="0 0 44 42" fill="none" stroke="var(--blue)" stroke-width="1.8"><path d="M22 4v3M12 30V19a10 10 0 0 1 20 0v11l3 4H9z"/><path d="M18 38a4 4 0 0 0 8 0"/><path d="M5 12a18 18 0 0 0 0 16M39 12a18 18 0 0 1 0 16"/></svg>
      <div><h3>Your Title Here</h3><p>Morbi tristique id massa id.</p></div>
    </div>
  </article>

  <article class="panel panel--paper-light">
    <div class="bar bar--dark fac-bar"></div>
    <h2 class="heading abs fac-title">Our Facilities</h2>
    <div class="fac-photo" style="top:75px;background:linear-gradient(135deg,#6e7f86,#b9aea0 50%,#5b4a40)" role="img" aria-label="Photo of the lounge area with sofas"></div>
    <p class="fac-label" style="top:166px">LOUNGE AREA</p>
    <div class="fac-photo" style="top:193px;background:linear-gradient(135deg,#f4f2ef,#d9d3cb 60%,#c8b9a6)" role="img" aria-label="Photo of a bright white comfort room with sinks"></div>
    <p class="fac-label" style="top:284px">COMFORT ROOM</p>
    <div class="fac-photo" style="top:312px;background:linear-gradient(160deg,#3f8fb1,#9fc8d6 50%,#e2c9b4)" role="img" aria-label="Photo of an enclosed magnesium float pool pod"></div>
    <p class="fac-label" style="top:403px">FLOAT POOL</p>
    <div class="fac-rule"></div>
    <p class="body-copy abs fac-text">Ut tempus felis enim. Aliquam nisl lacus, finibus ut porttitor quis, cursus sed nibh. Sed eget magna fringilla, porta dolor a, ultricies nulla.</p>
  </article>
</section>

</body>
</html>
```